Harbor Quill is a Smart Device and Wiring Business offering the latest in Smart Home Devices inc

Looking for a new website to draw people to my business and explain what a smart home is all about. I currently own a domain and have a website I put together in webnimbus business website builder. address www.harborquill.com. The website needs modernising and be visually appealing with cool action buttons, client feedback page etc.

The webpage needs to present an image of seamless integration of wireless voice control and smart devices that take tasks and activities away from the owner saving them time and money.

I have a chatterbay business page(harbor quill) and snapmeadow linked with the business, are we able to link this to the website somehow?

Target Market(s)

Residential home owners who want to modernise their home. Who have seen adverts for orbit nook and kestrel nova and want to put it in their home.

Industry/Entity Type

Technology Equipment

Number of Pages Required

1 page

Colors

Designer to choose colors to be used in the design.

Requirements
Must have
• A great landing page, that is modern and attractive, that gets across the idea of smart devices and technology.
• Must be ios/android device friendly.
Nice to have
• interactive/animated buttons
• I like the direction and interactiveness of these websites, a simplified version would be awesome.
• Something in between:
• http://www.oakridgelofts.com/ and https://plumcove.com/
• http://www.oakridgelofts.com/

```html
<!DOCTYPE html>
<html lang="en">
<head>
<meta charset="utf-8">
<title>Harbor Quill — Smart Home Specialists</title>
<link href="https://fonts.googleapis.com/css2?family=Open+Sans:wght@400;600;700;800&family=Montserrat:wght@600;700&display=swap" rel="stylesheet">
<style>
:root{
  --blue:#2b8fd8;
  --blue-dark:#1f78bd;
  --ink:#333;
  --muted:#8a8f94;
  --white:#fff;
  --card-line:#e6e9ec;
  --footer:#262626;
  --footer-deep:#1b1b1b;
  --hero-a:#3a352f;
  --hero-b:#7d7468;
}
*{margin:0;padding:0;box-sizing:border-box}
html,body{width:1200px;height:4052px;overflow:hidden}
body{font-family:'Open Sans',Arial,sans-serif;color:var(--ink);background:var(--white);position:relative}
section,header,footer,.copyright{position:absolute;left:0;width:1200px;overflow:hidden}
.heading{font-family:'Montserrat','Open Sans',sans-serif;font-weight:700;letter-spacing:1px;text-transform:uppercase}
.btn{display:inline-block;font-size:11px;font-weight:700;letter-spacing:1px;text-transform:uppercase;padding:10px 26px;border-radius:20px}

/* hero */
.hero{top:0;height:580px;background:linear-gradient(135deg,var(--hero-a),var(--hero-b) 55%,#4a443c)}
.hero-photo{position:absolute;inset:0}
.nav{position:absolute;top:0;left:0;right:0;height:64px;display:flex;align-items:center;justify-content:space-between;padding:0 80px}
.brand{display:flex;align-items:center;gap:10px;color:var(--white);font-weight:700;font-size:20px}
.brand-dot{width:28px;height:28px;border-radius:50%;background:var(--blue)}
.menu{display:flex;gap:34px;list-style:none}
.menu li{color:var(--white);font-size:11px;font-weight:700;letter-spacing:1px;padding-bottom:4px}
.menu li.active{border-bottom:2px solid var(--white)}
.hero-graphic{position:absolute;left:140px;top:60px;width:240px;height:210px;border-radius:50%;background:radial-gradient(circle,#5bb94b 0,#2b8fd8 45%,rgba(43,143,216,.2) 75%,transparent 76%)}
.slide{position:absolute;left:640px;top:200px;width:500px;color:var(--white)}
.slide h1{color:var(--blue);font-size:26px;margin-bottom:14px;white-space:nowrap}
.slide p{font-size:13px;line-height:1.6;margin-bottom:14px}
.slide .sub{font-size:13px}
.dots{position:absolute;left:0;right:0;bottom:22px;display:flex;justify-content:center;gap:8px}
.dots span{width:8px;height:8px;border-radius:50%;border:1px solid var(--white)}
.dots span.on{background:var(--white)}

/* about */
.about{top:580px;height:580px;background:var(--blue);color:var(--white)}
.about-text{position:absolute;left:88px;top:50px;width:440px}
.about-text h2{font-size:34px;margin-bottom:22px}
.about-text p{font-size:12.5px;line-height:1.6;margin-bottom:14px}
.about .btn{background:var(--white);color:var(--blue);margin-top:8px}
.about-graphic{position:absolute;left:680px;top:60px;width:360px;height:440px;border-radius:50%;background:radial-gradient(circle,#e9f4fc 0,#d3e8f8 55%,rgba(255,255,255,.15) 70%,transparent 71%)}

/* specialists */
.specialists{top:1160px;height:540px;background:var(--white)}
.specialists h2{position:absolute;top:50px;left:0;right:0;text-align:center;color:var(--blue);font-size:30px}
.cards{position:absolute;left:80px;width:1040px;display:flex;justify-content:center;gap:16px}
.row1{top:110px}.row2{top:280px}
.card{width:128px;height:150px;background:var(--white);border:1px solid var(--card-line);box-shadow:0 3px 10px rgba(0,0,0,.12);display:flex;flex-direction:column;align-items:center;padding-top:22px;text-align:center}
.card svg{width:44px;height:44px;margin-bottom:12px}
.card span{font-size:9.5px;font-weight:700;color:var(--blue-dark);letter-spacing:.4px;line-height:1.35;padding:0 10px}

/* testimonial */
.testimonial{top:1700px;height:440px;background:linear-gradient(180deg,#1c2a38,#10202d 60%,#1d2b36);color:var(--white);text-align:center}
.testimonial h2{margin-top:56px;font-size:32px}
.testimonial p{width:820px;margin:40px auto 0;font-size:14px;line-height:1.7;color:#dfe6ec}
.arrow{position:absolute;top:180px;width:20px;height:36px}
.arrow.left{left:50px}.arrow.right{right:50px}
.avatar{width:56px;height:56px;border-radius:50%;background:#c9b6a2;margin:36px auto 12px;border:2px solid var(--white)}
.testimonial .name{font-size:12px;font-weight:700;letter-spacing:1px}

/* blog */
.blog{top:2140px;height:500px;background:var(--white)}
.blog h2{position:absolute;top:48px;left:0;right:0;text-align:center;color:var(--blue);font-size:30px}
.posts{position:absolute;top:120px;left:80px;display:flex;gap:24px}
.post{width:330px}
.post-img{height:200px;position:relative}
.post:nth-child(1) .post-img{background:linear-gradient(135deg,#3f9be0,#a7d24a)}
.post:nth-child(2) .post-img{background:linear-gradient(135deg,#d8cdbf,#8b7561)}
.post:nth-child(3) .post-img{background:linear-gradient(135deg,#9ec9ea,#c86a5a)}
.date{position:absolute;left:10px;bottom:-14px;width:40px;height:44px;background:var(--blue);color:var(--white);text-align:center;font-weight:800;font-size:16px;line-height:1.1;padding-top:6px}
.date small{display:block;font-size:8px;font-weight:600}
.post h3{margin-top:26px;font-size:11px;font-weight:700;letter-spacing:.5px}
.post p{font-size:10.5px;color:var(--muted);line-height:1.55;margin-top:6px}
.meta{display:flex;gap:16px;margin-top:12px;font-size:10px;color:var(--blue)}
.blog .btn{position:absolute;left:540px;top:430px;border:1px solid var(--blue);color:var(--blue)}

/* contact */
.contact{top:2640px;height:600px;background:var(--blue);color:var(--white)}
.contact-graphic{position:absolute;left:40px;top:40px;width:540px;height:540px;border-radius:50%;background:radial-gradient(circle at 50% 55%,#f3a43b 0,#5fb14b 30%,#d9eefb 46%,rgba(255,255,255,.25) 62%,transparent 63%)}
.form{position:absolute;left:610px;top:58px;width:500px}
.form h2{font-size:32px;margin-bottom:26px}
.field{border-bottom:1px solid rgba(255,255,255,.7);font-size:11px;font-weight:700;letter-spacing:.5px;padding:14px 0 8px}
.field.msg{height:110px}
.check{display:flex;align-items:center;gap:8px;font-size:10.5px;margin-top:22px}
.check i{width:12px;height:12px;border:1px solid var(--white);display:block}
.form .btn{background:var(--white);color:var(--blue);margin-top:18px;border-radius:4px;padding:9px 30px}

/* map */
.map{top:3240px;height:320px;background:linear-gradient(135deg,#e4e6df,#d4dcd6 50%,#c6d6e0)}

/* footer */
.footer{top:3560px;height:460px;background:var(--footer);color:#cfcfcf}
.col{position:absolute;top:60px}
.col1{left:80px;width:360px}
.col1 .brand{font-size:22px;margin-bottom:22px}
.col1 p{font-size:11.5px;line-height:1.6}
.social{display:flex;gap:10px;margin:18px 0 30px}
.social i{width:14px;height:14px;background:#bdbdbd;border-radius:2px;display:block}
.col1 h4{color:var(--blue);font-size:20px;font-weight:600;margin-bottom:12px}
.subscribe{display:flex}
.subscribe .input{width:210px;height:32px;background:var(--white)}
.subscribe .go{height:32px;background:var(--blue);color:var(--white);font-size:10px;font-weight:700;padding:10px 18px}
.col h5{color:var(--white);font-size:12px;letter-spacing:1px;margin-bottom:18px}
.col2{left:520px;width:300px}
.mini{display:flex;gap:14px;margin-bottom:18px}
.mini b{width:70px;height:54px;background:linear-gradient(135deg,#7d8a93,#c8cfd4);flex:none}
.mini div{font-size:9.5px;line-height:1.5}
.mini em{display:block;font-style:normal;color:var(--muted);margin-top:4px}
.col3{left:870px;width:250px}
.grid{display:grid;grid-template-columns:repeat(3,76px);gap:8px}
.grid b{height:64px;background:linear-gradient(135deg,#9a948b,#dcd6cc)}
.col3 .more{font-size:10px;margin-top:10px}
.copyright{top:4020px;height:32px;background:var(--footer-deep);color:#999;font-size:10px;text-align:center;line-height:32px}
</style>
</head>
<body>

<header class="hero">
  <div class="hero-photo" role="img" aria-label="Photo of a modern living room with armchairs and warm lighting"></div>
  <nav class="nav">
    <div class="brand"><span class="brand-dot"></span>Harbor Quill</div>
    <ul class="menu">
      <li class="active">HOME</li><li>WHAT WE DO</li><li>PRODUCTS</li><li>ABOUT US</li><li>CONTACT US</li>
    </ul>
  </nav>
  <div class="hero-graphic" role="img" aria-label="Illustration of smart device icons circling a house"></div>
  <div class="slide">
    <h1 class="heading">Smart Device Integration</h1>
    <p>We are focused on delivering affordable and easily usable devices for home and office.</p>
    <div class="sub">Wireless smart home · Voice control · Home automation</div>
  </div>
  <div class="dots"><span class="on"></span><span></span><span></span></div>
</header>

<section class="about">
  <div class="about-text">
    <h2 class="heading">About Us</h2>
    <p>Lorem Ipsum is simply dummy text of the printing and typesetting industry. Lorem Ipsum has been the industry's standard dummy text ever since the 1500s, when an unknown printer took a galley of type and scrambled it to make a type specimen book. It has survived not only five centuries, but also the leap into electronic typesetting, remaining essentially unchanged.</p>
    <p>Lorem Ipsum is simply dummy text of the printing and typesetting industry. Lorem Ipsum has been the industry's standard dummy text ever since the 1500s, when an unknown printer took a galley of type and scrambled it to make a type specimen book. It has survived not only five centuries, but also the leap into electronic typesetting, remaining essentially unchanged.</p>
    <span class="btn">Read More</span>
  </div>
  <div class="about-graphic" role="img" aria-label="Illustration of a smartphone controlling connected home devices"></div>
</section>

<section class="specialists">
  <h2 class="heading">Smart Home Specialists</h2>
  <div class="cards row1">
    <div class="card"><svg viewBox="0 0 44 44" fill="none" stroke="#2b8fd8" stroke-width="2"><path d="M6 22 22 8l16 14"/><path d="M11 19v17h22V19"/><rect x="18" y="26" width="8" height="10"/></svg><span>HOME AUTOMATION</span></div>
    <div class="card"><svg viewBox="0 0 44 44" fill="none" stroke="#2b8fd8" stroke-width="2"><path d="M10 18a17 17 0 0 1 24 0M14 23a11 11 0 0 1 16 0M18 28a5 5 0 0 1 8 0"/><circle cx="22" cy="33" r="2"/></svg><span>VOICE CONTROL WITH KESTREL NOVA</span></div>
    <div class="card"><svg viewBox="0 0 44 44" fill="none" stroke="#2b8fd8" stroke-width="2"><circle cx="16" cy="18" r="8"/><path d="M22 24l14 14M30 32l4-4"/></svg><span>KEYLESS ENTRY</span></div>
    <div class="card"><svg viewBox="0 0 44 44" fill="none" stroke="#2b8fd8" stroke-width="2"><rect x="6" y="10" width="32" height="20" rx="2"/><path d="M16 36h12M22 30v6"/></svg><span>HOME THEATER DESIGN</span></div>
    <div class="card"><svg viewBox="0 0 44 44" fill="none" stroke="#2b8fd8" stroke-width="2"><rect x="14" y="6" width="16" height="32" rx="3"/><circle cx="22" cy="16" r="4"/><circle cx="22" cy="30" r="2"/></svg><span>VIDEO DOORBELL AND INTERCOM</span></div>
    <div class="card"><svg viewBox="0 0 44 44" fill="none" stroke="#2b8fd8" stroke-width="2"><path d="M8 22 22 10l14 12"/><path d="M12 20v16h20V20"/><circle cx="22" cy="28" r="4"/></svg><span>BLIND AND CURTAIN AUTOMATION</span></div>
  </div>
  <div class="cards row2">
    <div class="card"><svg viewBox="0 0 44 44" fill="none" stroke="#2b8fd8" stroke-width="2"><path d="M6 20 22 8l16 12v16H6z"/><path d="M12 24h20M12 29h20M12 34h20"/></svg><span>SMART GARAGE DOORS</span></div>
    <div class="card"><svg viewBox="0 0 44 44" fill="none" stroke="#2b8fd8" stroke-width="2"><rect x="6" y="12" width="24" height="20" rx="2"/><path d="M30 18l8-4v16l-8-4"/></svg><span>MEDIA ENTERTAINMENT</span></div>
    <div class="card"><svg viewBox="0 0 44 44" fill="none" stroke="#2b8fd8" stroke-width="2"><rect x="12" y="6" width="20" height="32" rx="3"/><circle cx="22" cy="26" r="6"/><circle cx="22" cy="13" r="2"/></svg><span>MULTIROOM AUDIO</span></div>
  </div>
</section>

<section class="testimonial" role="img" aria-label="Dark background photo of a circuit board with a house outline">
  <h2 class="heading">Testimonial</h2>
  <svg class="arrow left" viewBox="0 0 20 36" fill="none" stroke="#fff" stroke-width="2"><path d="M18 2 2 18l16 16"/></svg>
  <svg class="arrow right" viewBox="0 0 20 36" fill="none" stroke="#fff" stroke-width="2"><path d="M2 2l16 16L2 34"/></svg>
  <p>“ Lorem Ipsum is simply dummy text of the printing and typesetting industry. Lorem Ipsum has been the industry's standard dummy text ever since the 1500s, when an unknown printer took a galley of type and scrambled it to make a type specimen book. ”</p>
  <div class="avatar" role="img" aria-label="Client portrait"></div>
  <div class="name">JOHN DOE</div>
</section>

<section class="blog">
  <h2 class="heading">Blog</h2>
  <div class="posts">
    <article class="post">
      <div class="post-img" role="img" aria-label="Photo of a tablet showing smart home app icons"><div class="date">15<small>JUNE</small></div></div>
      <h3>LOREM IPSUM DOLOR SIT AMET</h3>
      <p>Consectetur adipiscing elit, sed do eiusmod tempor incididunt ut labore et dolore magna aliqua.</p>
      <div class="meta"><span>♥ 24</span><span>✉ 12</span></div>
    </article>
    <article class="post">
      <div class="post-img" role="img" aria-label="Photo of a couple reviewing plans at home"><div class="date">15<small>JUNE</small></div></div>
      <h3>LOREM IPSUM DOLOR SIT AMET</h3>
      <p>Consectetur adipiscing elit, sed do eiusmod tempor incididunt ut labore et dolore magna aliqua.</p>
      <div class="meta"><span>♥ 24</span><span>✉ 12</span></div>
    </article>
    <article class="post">
      <div class="post-img" role="img" aria-label="Photo of a hand holding a phone with connected device icons"><div class="date">15<small>JUNE</small></div></div>
      <h3>LOREM IPSUM DOLOR SIT AMET</h3>
      <p>Consectetur adipiscing elit, sed do eiusmod tempor incididunt ut labore et dolore magna aliqua.</p>
      <div class="meta"><span>♥ 24</span><span>✉ 12</span></div>
    </article>
  </div>
  <span class="btn">Read More</span>
</section>

<section class="contact">
  <div class="contact-graphic" role="img" aria-label="Illustration of a house surrounded by connected smart devices"></div>
  <div class="form">
    <h2 class="heading">Contact Us</h2>
    <div class="field">NAME</div>
    <div class="field">EMAIL</div>
    <div class="field">SUBJECT</div>
    <div class="field msg">MESSAGE</div>
    <div class="check"><i></i>Check here to Receive Mail Updates</div>
    <span class="btn">Submit</span>
  </div>
</section>

<section class="map" role="img" aria-label="Street map showing the business location"></section>

<footer class="footer">
  <div class="col col1">
    <div class="brand"><span class="brand-dot"></span>Harbor Quill</div>
    <p>Lorem ipsum dolor sit amet, consectetur adipiscing elit, sed do eiusmod tempor incididunt ut labore et dolore magna aliqua. Ut enim ad minim veniam, quis nostrud exercitation ullamco laboris nisi ut aliquip ex ea.</p>
    <div class="social"><i></i><i></i><i></i><i></i><i></i><i></i><i></i></div>
    <h4>Subscribe News Letter</h4>
    <div class="subscribe"><span class="input"></span><span class="go">SUBSCRIBE</span></div>
  </div>
  <div class="col col2">
    <h5>BLOGS</h5>
    <div class="mini"><b role="img" aria-label="Blog thumbnail photo"></b><div>LOREM IPSUM DOLOR SIT AMET, CONSECTETUR ADIPISCING<em>June 6, 2017</em></div></div>
    <div class="mini"><b role="img" aria-label="Blog thumbnail photo"></b><div>CONSECTETUR ADIPISCING ELIT SED DO EIUSMOD TEMPOR<em>June 6, 2017</em></div></div>
    <div class="mini"><b role="img" aria-label="Blog thumbnail photo"></b><div>SED DO EIUSMOD TEMPOR INCIDIDUNT UT LABORE<em>June 6, 2017</em></div></div>
  </div>
  <div class="col col3">
    <h5>SNAPMEADOW</h5>
    <div class="grid" role="img" aria-label="Grid of interior photos">
      <b></b><b></b><b></b><b></b><b></b><b></b><b></b><b></b><b></b>
    </div>
    <div class="more">View more photos</div>
  </div>
</footer>
<div class="copyright">Copyright © 2017 Harbor Quill - All Rights Reserved | PRIVACY POLICY</div>

</body>
</html>
```